Bonusheft für Patienten als kleine DIN A6 Broschüre
Zielgruppe
Bonusheft für Patienten als kleine DIN A6 Broschüre in der Zahn-Prophylaxe. Die Texte haben wir bereits vollständig formuliert, auch die Gliederung ist vorgegeben.
Wir sind eine Zahnarztpraxis mit dem Schwerpunkt Prophylaxe. Für unsere Prophylaxeabteilung möchten wir eine DIN A6 Broschüre entwerfen lassen, die als Bonusheft für Patienten dient.
Inhalt: Informationen über unsere Praxis, die leitende Mitarbeiterin, individuelle Risiken und Empfehlungen der Patienten. Auch Fakten und Tipps zur Verbesserung der Mundhygiene und Putzgewohnheiten werden Beschrieben.
Aufgabenstellung
Broschüre als DIN A6 Bonusheft mit circa sieben gestalteten Seiten, bei denen wir den Aufbau und die exakten Texte bereits vollständig vorgeben. Zusätzlich folgen mehrere gleiche Seiten, bei denen die Termine und Stempel eingetragen werden (ca. fünf Seiten).
Für Ihre Orientierung haben wir unsere Fotos und Farbschema von vorhandenen Designs unserer Praxis bereitgestellt.
Orientieren Sie sich gerne an unserer vorhandenen Homepage im Hinblick auf unseren Stil und das Praxislogo.
Homepage: www.zahnpraxis-am-lindenhof.de
Wir stellen einige Fotos zur Verwendung bereit. Falls nötig, verwenden Sie auch Stock Fotos.
Im folgenden werden wir den gewünschten Aufbau mit den Texten je Seite detailliert vorstellen. Ihre Aufgabe ist es, dies in ein modernes, frisches, ansprechendes und kompetentes Design umzusetzen.
1. Seite / Cover
- Mit Praxislogo
- Text: „Mein Prophylaxepass“
2. Seite:
- Überschrift: „Sie lassen nicht jeden an Ihre Zähne? Wir auch nicht.“
-Text: „Herzlich Willkommen! Mein Name ist Merle und ich arbeite als leitende Mitarbeiterin im Lindenhof Zentrum Hagenfeld. Momentan befinde ich mich in der Weiterbildung zur Dentalhygienikerin und bin begeistert von der Arbeit in der präventiven Zahnmedizin. Mit meinem Wissen und meiner Erfahrung möchte ich dazu beitragen, dass unsere Patienten sich bei uns wohl und gut betreut fühlen. Ich freue mich darauf, Ihnen zu helfen, Ihre Zahngesundheit zu erhalten und zu verbessern!“
- Foto einer Mitarbeiterin
4. Seite:
- Überschrift: „Die professionelle Zahnreinigung – Wellness & Prävention“
- Text: „Eine wichtige Präventionsmaßnahme ist die regelmäßige Zahnreinigung in unserem Prophylaxe-Zentrum. Karies, Mundgeruch und Zahnfleischerkrankungen werden effektiv vorgebeugt. Die Zahnreinigung ist ein Teil der individuell geplanten Prophylaxe und eine sinnvolle Ergänzung der häus..

```html
<!DOCTYPE html>
<html lang="de">
<head>
<meta charset="utf-8">
<title>Mein Prophylaxepass – Seitenübersicht</title>
<link rel="stylesheet" href="https://fonts.googleapis.com/css2?family=Arimo:wght@400;700&family=Questrial&display=swap">
<style>
  :root {
    --stage: #000;
    --paper: #fff;
    --ink: #1a1a1a;
    --sand: #cfc9ac;
    --label: #fff;
  }
  * { box-sizing: border-box; margin: 0; padding: 0; }
  html, body { width: 1200px; height: 969px; overflow: hidden; background: var(--stage); }
  body { position: relative; font-family: "Arimo", Arial, sans-serif; color: var(--ink); }

  .page { position: absolute; width: 286px; height: 402px; background: var(--paper); overflow: hidden; }
  .band { position: absolute; left: 0; right: 0; height: 7px; background: var(--sand); }
  .band--top { top: 9px; }
  .band--bottom { top: 386px; }

  .page-label { position: absolute; width: 286px; text-align: center; color: var(--label);
    font: 700 21px/1 "Arimo", Arial, sans-serif; }

  .abs { position: absolute; }
  .heading { font-weight: 700; font-size: 13.5px; letter-spacing: .2px; }
  .body-copy { font-size: 10.8px; line-height: 13.8px; }
  .photo { position: absolute; }

  /* Cover */
  .cover-square { position: absolute; left: 116px; top: 18px; width: 54px; height: 54px; background: var(--sand); }
  .cover-rule { position: absolute; height: 2px; background: var(--sand); }
  .brand-name { position: absolute; left: 0; right: 0; text-align: center; font-family: "Questrial", "Century Gothic", sans-serif; color: var(--ink); font-weight: 400; }
  .cover-doctors { position: absolute; left: 0; right: 0; top: 201px; text-align: center;
    font-family: "Questrial", "Century Gothic", sans-serif; font-size: 15px; }
  .cover-photo { left: 0; top: 229px; width: 286px; height: 173px;
    background: linear-gradient(180deg, #e6e6e6 0%, #bdbdbd 35%, #5b5b5b 60%, #8a8a8a 100%); }
  .cover-title { position: absolute; left: 0; right: 0; top: 235px; text-align: center;
    font: 700 21px/1 "Arimo", Arial, sans-serif; color: var(--sand); letter-spacing: .3px;
    text-shadow: 0 0 1px #555, 0 0 1px #555; }

  /* Checklists */
  .checklist { position: absolute; list-style: none; }
  .checklist li { position: relative; height: 20px; line-height: 20px; font-size: 12.2px; }
  .checkbox { position: absolute; top: 3px; width: 14px; height: 14px; border: 1.3px solid var(--ink); }
  .decor { position: absolute; left: 0; right: 0; top: 262px; text-align: center; }
  .decor-square { display: inline-block; width: 64px; height: 64px; background: var(--sand); vertical-align: middle; }
  .decor-name { display: block; margin-top: 10px; font: 400 15px/1.2 "Arimo", Arial, sans-serif; color: var(--sand); }

  /* Appointment forms */
  .ln { position: absolute; left: 8px; font-size: 10.8px; line-height: 12px; white-space: nowrap; }
  .ln b { font-weight: 700; }
  .ln.indent { left: 21px; }
  .ln .gap { display: inline-block; width: 24px; }
  .blank { display: inline-block; width: 95px; border-bottom: 1px solid var(--ink); height: 9px; vertical-align: baseline; margin-left: 4px; }
  .divider { position: absolute; left: 8px; right: 8px; height: 2px; background: var(--ink); }
</style>
</head>
<body>

<!-- Seite 1 / Cover -->
<section class="page" style="left:12px; top:12px;">
  <div class="cover-square"></div>
  <div class="cover-rule" style="left:9px; width:68px; top:80px;"></div>
  <div class="cover-rule" style="left:208px; width:68px; top:80px;"></div>
  <div class="brand-name" style="top:92px; font-size:37px; line-height:1;">Zahnpraxis</div>
  <div class="brand-name" style="top:140px; font-size:26px; line-height:1;">am Lindenhof</div>
  <div class="cover-rule" style="left:9px; width:268px; top:186px;"></div>
  <div class="cover-doctors">Dr. Jonas &amp; Lukas Brenner mit Team</div>
  <div class="photo cover-photo" role="img" aria-label="Schwarzweißfoto des Praxisgebäudes aus Backstein"></div>
  <div class="cover-title">Mein Prophylaxepass</div>
</section>
<div class="page-label" style="left:12px; top:427px;">Seite 1 / Cover</div>

<!-- Seite 2 -->
<section class="page" style="left:311px; top:12px;">
  <div class="band band--top"></div>
  <div class="abs heading" style="left:8px; top:33px; font-size:13.2px;">Sie lassen nicht jeden an Ihre Zähne?</div>
  <div class="abs heading" style="left:8px; top:66px; font-size:13px;">Wir auch nicht.</div>
  <div class="photo" style="left:138px; top:65px; width:135px; height:136px; background:linear-gradient(160deg,#8d8d8d,#5e6a66 60%,#3f6b5e);" role="img" aria-label="Foto der leitenden Prophylaxe-Mitarbeiterin mit Zahnmodell"></div>
  <div class="abs body-copy" style="left:9px; top:206px; width:268px;">
    <b>Herzlich Willkommen!</b><br>
    Mein Name ist Merle und ich arbeite als leitende Mitarbeiterin im Lindenhof Zentrum Hagenfeld. Momentan befinde ich mich in der Weiterbildung zur Dentalhygienikerin und bin begeistert von der Arbeit in der präventiven Zahnmedizin. Mit meinem Wissen und meiner Erfahrung möchte ich dazu beitragen, dass unsere Patienten sich bei uns wohl und gut betreut fühlen. Ich freue mich darauf, Ihnen zu helfen, Ihre Zahngesundheit zu erhalten und zu verbessern!
  </div>
  <div class="band band--bottom"></div>
</section>
<div class="page-label" style="left:298px; top:425px;">Seite 2</div>

<!-- Seite 3 -->
<section class="page" style="left:608px; top:12px;">
  <div class="band band--top"></div>
  <div class="abs heading" style="left:8px; top:19px; font-size:13.8px;">Die professionelle Zahnreinigung</div>
  <div class="abs heading" style="left:8px; top:39px; font-size:12.6px;">Wellness &amp; Prävention</div>
  <div class="abs body-copy" style="left:8px; top:58px; width:276px;">
    Eine wichtige Präventionsmaßnahme ist die regelmäßige Zahnreinigung in unserem Prophylaxe-Zentrum.<br>
    Karies, Mundgeruch und Zahnfleischerkrankungen werden effektiv vorgebeugt. Die Zahnreinigung ist ein Teil der individuell geplanten Prophylaxe und eine sinnvolle Ergänzung der häuslichen Zahnpflege, gerade an den Stellen, wo die eigene Zahnbürste nicht hinkommt. Schonend werden alle harten und weichen Beläge von allen Zahnoberflächen entfernt — inklusive Kaffee-, Tee- und Raucherbelägen.
  </div>
  <div class="photo" style="left:75px; top:217px; width:135px; height:90px; background:linear-gradient(135deg,#dfe6ea,#8fa9b8 55%,#2d2f36);" role="img" aria-label="Foto einer Familie im Gespräch mit dem Zahnarzt"></div>
  <div class="abs body-copy" style="left:8px; top:314px; width:276px;">
    Natürlich weiße Zähne ! Nach der professionellen Zahnreinigung stellt sich Ihre natürliche Zahnfarbe wieder ein und ein frisches Mundgefühl entsteht.<br>
    In den meisten Fällen werden die Zähne nach der Prophylaxe heller. Erhöhen Sie Ihre Lebensqualität!
  </div>
  <div class="band band--bottom"></div>
</section>
<div class="page-label" style="left:595px; top:427px;">Seite 3</div>

<!-- Seite 4 -->
<section class="page" style="left:902px; top:12px;">
  <div class="band band--top"></div>
  <div class="abs heading" style="left:8px; top:22px; font-size:13.8px; line-height:17px;">Moderne Technik für eine<br>bessere Behandlung</div>
  <div class="abs body-copy" style="left:8px; top:62px; width:276px;">
    Für unsere Prophylaxebehandlungen nutzen wir aktuelle Behandlungsmethoden und bedienen uns neuer Technologie wie der Pulsejet Prophylaxe-Station.<br>
    Dadurch gewährleisten wir für unsere Patienten eine leise und angenehme Behandlung. Gleichzeitig stellen wir eine ausgezeichnete Behandlungsqualität sicher, welche Ihre Zähne nachhaltig schützt und Krankheiten vorbeugt.
  </div>
  <div class="photo" style="left:0; top:190px; width:286px; height:190px; background:linear-gradient(120deg,#2a8fc0,#bfe0ee 45%,#e8d7b8 70%,#6fb6d6);" role="img" aria-label="Foto einer lächelnden Patientin im Behandlungsstuhl mit Zahnfarbskala"></div>
  <div class="band band--bottom"></div>
</section>
<div class="page-label" style="left:889px; top:425px;">Seite 4</div>

<!-- Seite 5 -->
<section class="page" style="left:12px; top:506px;">
  <div class="band band--top"></div>
  <div class="abs heading" style="left:8px; top:24px; font-size:13.8px;">Risikoanalyse</div>
  <ul class="checklist" style="left:50px; top:65px;">
    <li><span class="checkbox"></span><span style="margin-left:26px;">Karisaktivität</span></li>
    <li><span class="checkbox"></span><span style="margin-left:26px;">Empfindliches Zahnfleisch</span></li>
    <li><span class="checkbox"></span><span style="margin-left:26px;">Erosionen / Säureschäden</span></li>
    <li><span class="checkbox"></span><span style="margin-left:26px;">Zahnschmelzverlust</span></li>
    <li><span class="checkbox"></span><span style="margin-left:26px;">Weicher Zahnschmelz</span></li>
    <li><span class="checkbox"></span><span style="margin-left:26px;">Halitosis (Mundgeruch)</span></li>
    <li><span class="checkbox"></span><span style="margin-left:26px;">Zahnverfärbungen</span></li>
    <li><span class="checkbox"></span><span style="margin-left:26px;">Rauchen</span></li>
    <li><span class="checkbox"></span><span style="margin-left:26px;">Retainer</span></li>
  </ul>
  <div class="decor"><span class="decor-square"></span><span class="decor-name">Zahnpraxis am Lindenhof</span></div>
  <div class="band band--bottom"></div>
</section>
<div class="page-label" style="left:12px; top:926px;">Seite 5</div>

<!-- Seite 6 -->
<section class="page" style="left:310px; top:506px;">
  <div class="band band--top"></div>
  <div class="abs heading" style="left:8px; top:24px; font-size:13.8px;">Ergänzende Pflegetipps</div>
  <ul class="checklist" style="left:17px; top:65px;">
    <li><span class="checkbox"></span><span style="margin-left:26px;">1. Zahnseide</span></li>
    <li><span class="checkbox"></span><span style="margin-left:26px;">2. Superfloss</span></li>
    <li><span class="checkbox"></span><span style="margin-left:26px;">3. Zahnseidesticks</span></li>
    <li><span class="checkbox"></span><span style="margin-left:26px;">4. Interdentalbürstchen</span></li>
    <li><span class="checkbox"></span><span style="margin-left:26px;">5. Zungenreinigung</span></li>
    <li><span class="checkbox"></span><span style="margin-left:26px;">6. Intensiv Fluoridierung</span></li>
    <li><span class="checkbox"></span><span style="margin-left:26px;">7. 1x wöchentliche Spezial Zahnpasta</span></li>
    <li><span class="checkbox"></span><span style="margin-left:26px;">8. Munddusche</span></li>
    <li><span class="checkbox"></span><span style="margin-left:26px;">9. Mundspüllösung</span></li>
  </ul>
  <div class="decor"><span class="decor-square"></span><span class="decor-name">Zahnpraxis am Lindenhof</span></div>
  <div class="band band--bottom"></div>
</section>
<div class="page-label" style="left:320px; top:926px;">Seite 6</div>

<!-- Seite 7 -->
<section class="page" style="left:608px; top:506px;">
  <div class="band band--top"></div>
  <div class="ln" style="top:25px;">Prophylaxe Pass überreicht am: <span class="blank" style="width:76px;"></span></div>
  <div class="ln" style="top:43px;"><b>Ihr Intervall:</b></div>
  <div class="ln" style="top:60px;">O 3 Monate&nbsp; O 4 Monate&nbsp; O 6 Monate&nbsp; O 12 Monate</div>
  <div class="ln" style="top:81px;"><b>Heutiger Termin:</b></div>
  <div class="ln" style="top:102px;">Intervall:</div>
  <div class="ln indent" style="left:20px; top:115px;">O 3 Monate O 4 Monate O 6 Monate O 12 Monate</div>
  <div class="ln" style="top:130px;">Terminart:</div>
  <div class="ln indent" style="top:144px;">O Regulärer Termin<span class="gap"></span>O Kompakttermin</div>
  <div class="ln" style="top:170px;">Datum | Uhrzeit: <span class="blank"></span></div>
  <div class="ln" style="top:190px;">Behandelt von: <span class="blank" style="margin-left:10px;"></span></div>
  <div class="divider" style="top:214px;"></div>
  <div class="ln" style="top:230px;"><b>Ihr nächster Termin:</b></div>
  <div class="ln" style="top:251px;"><b>Ihr Intervall:</b></div>
  <div class="ln" style="top:268px;">O 3 Monate&nbsp; O 4 Monate&nbsp; O 6 Monate&nbsp; O 12 Monate</div>
  <div class="ln" style="top:295px;">Terminart:</div>
  <div class="ln indent" style="top:309px;">O Regulärer Termin<span class="gap"></span>O Kompakttermin</div>
  <div class="ln" style="top:335px;">Datum | Uhrzeit: <span class="blank"></span></div>
  <div class="ln" style="top:355px;">Behandelt von: <span class="blank" style="margin-left:10px;"></span></div>
  <div class="band band--bottom"></div>
</section>
<div class="page-label" style="left:618px; top:926px;">Seite 7</div>

<!-- Seite 8-12 -->
<section class="page" style="left:902px; top:506px;">
  <div class="band band--top"></div>
  <div class="ln" style="top:17px;"><b>Weitere Termine:</b></div>
  <div class="ln" style="top:35px;">Intervall:</div>
  <div class="ln" style="top:53px;">O 3 Monate&nbsp; O 4 Monate&nbsp; O 6 Monate&nbsp; O 12 Monate</div>
  <div class="ln" style="top:67px;">Terminart:</div>
  <div class="ln indent" style="left:20px; top:81px;">O Regulärer Termin<span class="gap"></span>O Kompakttermin</div>
  <div class="ln" style="top:102px;">Datum | Uhrzeit: <span class="blank"></span></div>
  <div class="ln" style="top:123px;">Behandelt von: <span class="blank" style="margin-left:10px;"></span></div>
  <div class="divider" style="top:141px;"></div>
  <div class="ln" style="top:152px;">Intervall:</div>
  <div class="ln" style="top:170px;">O 3 Monate&nbsp; O 4 Monate&nbsp; O 6 Monate&nbsp; O 12 Monate</div>
  <div class="ln" style="top:185px;">Terminart:</div>
  <div class="ln indent" style="left:20px; top:198px;">O Regulärer Termin<span class="gap"></span>O Kompakttermin</div>
  <div class="ln" style="top:220px;">Datum | Uhrzeit: <span class="blank"></span></div>
  <div class="ln" style="top:240px;">Behandelt von: <span class="blank" style="margin-left:10px;"></span></div>
  <div class="divider" style="top:262px;"></div>
  <div class="ln" style="top:273px;">Intervall:</div>
  <div class="ln" style="top:290px;">O 3 Monate&nbsp; O 4 Monate&nbsp; O 6 Monate&nbsp; O 12 Monate</div>
  <div class="ln" style="top:305px;">Terminart:</div>
  <div class="ln indent" style="left:20px; top:319px;">O Regulärer Termin<span class="gap"></span>O Kompakttermin</div>
  <div class="ln" style="top:340px;">Datum | Uhrzeit: <span class="blank"></span></div>
  <div class="ln" style="top:360px;">Behandelt von: <span class="blank" style="margin-left:10px;"></span></div>
  <div class="band band--bottom"></div>
</section>
<div class="page-label" style="left:897px; top:927px;">Seite 8-12</div>

</body>
</html>
```